Vintage themed home decor Shopify store needs sales promotion banner ads

"Quill & Lantern Goods" is an Australian based lifestyle home decor store that sells vintage, retro and antique relic replicas and reproduction items online to their local customers Australia wide.

We need banner ads for our store home page slider that promotes our unique products, new stock arrival and calls store visitors to to buy from our different product collections.

We anticipate that we will need multiple banner ads, primarily for the following product collections:
1. Sundials & Compass
2. Airplane models
3. Magnifying glass
4. Clocks & Watches

Banners could also be generic with generic discount coupon promotions.

Banners should be based around the theme of our store and products which gives a sense of colonial / vintage lifestyle and that they compliment the colour & theme of the store.

Banner Size: 1600 x 800 px

Please find attached some samples of the types of banner ads we have in mind and also our logo. Product images can be supplied if they are required to be used in the ads.

Website URL: https://quillandlanterngoods.example

Target Market(s)

mostly Males aged between 35-65.
Products ideally for man-cave & office decor.

Industry/Entity Type

Home And Garden

Font styles to use
Serif
Decorative
Script

Requirements
Must have
• some product images
Nice to have
• lifestyle shots.
• blank space to insert for a coupon code
Should not have
• caricatures & cartoon

```html
<!DOCTYPE html>
<html lang="en">
<head>
<meta charset="UTF-8">
<title>Compass &amp; Sundials – 5% Off – Quill &amp; Lantern Goods</title>
<link rel="stylesheet" href="https://fonts.googleapis.com/css2?family=Cinzel:wght@500;700&family=Roboto:wght@300;400;700&display=swap">
<style>
  :root {
    --parchment: #f4ebd8;
    --parchment-deep: #e9dcc0;
    --ink-brown: #5b2510;
    --band-brown: #5a2612;
    --band-edge: #7a3a1e;
    --cream: #f8eedb;
    --gold-line: #c9b27c;
    --coupon-tan: #a27d5d;
    --button-brown: #55240f;
    --button-shadow: #2e1206;
    --wood: #8a4424;
    --wood-dark: #4f200e;
    --brass: #b8985a;
    --felt: #1f3a2c;
  }
  * { margin: 0; padding: 0; box-sizing: border-box; }
  html, body { width: 1200px; height: 600px; overflow: hidden; background: var(--parchment); }
  .banner {
    position: relative;
    width: 1200px;
    height: 600px;
    overflow: hidden;
    background:
      radial-gradient(ellipse at 30% 40%, rgba(255,255,255,0.55), transparent 60%),
      linear-gradient(135deg, var(--parchment) 0%, var(--parchment-deep) 100%);
    font-family: 'Roboto', Arial, sans-serif;
  }
  .map-texture {
    position: absolute; inset: 0;
    background: radial-gradient(circle at 20% 70%, rgba(180,160,120,0.12), transparent 45%),
                radial-gradient(circle at 60% 20%, rgba(180,160,120,0.10), transparent 40%);
  }
  .frame-corner { position: absolute; left: 0; top: 0; }
  .product-photo {
    position: absolute;
    left: 500px; top: 0;
    width: 700px; height: 600px;
    clip-path: polygon(14% 22%, 100% 0, 100% 100%, 22% 100%, 6% 70%);
    background:
      radial-gradient(ellipse at 55% 50%, var(--brass) 0%, #8e7444 30%, var(--felt) 52%, transparent 60%),
      linear-gradient(160deg, var(--wood) 0%, var(--wood-dark) 100%);
  }
  .lion {
    position: absolute;
    top: 55px;
    width: 88px; height: 127px;
    border-radius: 40% 40% 20% 20%;
    background: linear-gradient(180deg, #7a3418, var(--ink-brown));
    opacity: 0.9;
  }
  .lion--left { left: 78px; }
  .lion--right { left: 442px; }
  .discount {
    position: absolute;
    left: 176px; top: 40px;
    color: var(--ink-brown);
    font-family: 'Cinzel', Georgia, serif;
    font-weight: 500;
  }
  .discount__number { position: absolute; left: 0; top: 0; font-size: 172px; line-height: 1; }
  .discount__percent { position: absolute; left: 108px; top: 22px; font-size: 56px; line-height: 1; }
  .discount__off { position: absolute; left: 102px; top: 82px; font-size: 66px; line-height: 1; }
  .collection-band {
    position: absolute;
    left: 0; top: 216px;
    width: 582px; height: 72px;
    background: var(--band-brown);
    border-top: 2px solid var(--band-edge);
    border-bottom: 2px solid var(--band-edge);
    box-shadow: 0 -7px 0 -4px var(--band-brown), 0 7px 0 -4px var(--band-brown);
    display: flex; align-items: center; justify-content: center;
    color: var(--cream);
    font-family: 'Cinzel', Georgia, serif;
    font-weight: 700;
    font-size: 40px;
    letter-spacing: 0.5px;
  }
  .coupon {
    position: absolute;
    left: 148px; top: 311px;
    width: 263px; height: 129px;
    background: var(--coupon-tan);
    color: var(--cream);
    text-align: center;
    padding-top: 16px;
  }
  .coupon__label { font-size: 19px; font-weight: 300; letter-spacing: 0.5px; line-height: 1.1; }
  .coupon__code { font-size: 37px; font-weight: 400; line-height: 1.1; }
  .coupon__expiry { font-size: 14px; font-weight: 700; margin-top: 3px; }
  .shop-button {
    position: absolute;
    left: 148px; top: 464px;
    width: 263px; height: 74px;
    background: var(--button-brown);
    box-shadow: 5px 5px 0 var(--button-shadow);
    color: var(--cream);
    font-size: 42px;
    font-weight: 400;
    display: flex; align-items: center; justify-content: center;
    text-decoration: none;
  }
</style>
</head>
<body>
  <div class="banner">
    <div class="map-texture" role="img" aria-label="Faint antique world map backdrop"></div>

    <svg class="frame-corner" width="1200" height="600" viewBox="0 0 1200 600" aria-hidden="true">
      <g fill="none" stroke="var(--gold-line)" stroke-width="2">
        <polyline points="26,178 26,30 365,30"/>
        <polyline points="34,120 34,38 100,38"/>
        <polyline points="42,70 42,46 66,46 66,58 54,58"/>
        <polyline points="26,420 26,563 390,563"/>
        <polyline points="34,480 34,555 100,555"/>
        <polyline points="42,530 42,547 66,547 66,535 54,535"/>
      </g>
    </svg>

    <div class="product-photo" role="img" aria-label="Antique brass triangular sundial compass in an open wooden presentation box lined with green felt"></div>

    <div class="lion lion--left" role="img" aria-label="Heraldic rampant lion emblem"></div>
    <div class="lion lion--right" role="img" aria-label="Heraldic rampant lion emblem"></div>

    <div class="discount">
      <span class="discount__number">5</span>
      <span class="discount__percent">%</span>
      <span class="discount__off">OFF</span>
    </div>

    <div class="collection-band">Compass &amp; Sundials</div>

    <div class="coupon">
      <div class="coupon__label">COUPON CODE</div>
      <div class="coupon__code">123BCD789</div>
      <div class="coupon__expiry">EXP. 18/08/2018</div>
    </div>

    <a class="shop-button" href="https://quillandlanterngoods.example">SHOP NOW</a>
  </div>
</body>
</html>
```